Marlow Crest Homes Needs Business Card Design

Looking for a unique modern business card to fit my new Logo.
Name: Dean Marlow
Company: Marlow Crest Homes, LLC
Tag Line: Forever Framed Right
Email: marlowcresthomes@mailvista.test
Phone: (253) 555-0187
Website: www.marlowcresthomes.test
License: MARLOCH462QT

```html
<!DOCTYPE html>
<html lang="en">
<head>
<meta charset="utf-8">
<title>Marlow Crest Homes – Business Card</title>
<link rel="stylesheet" href="https://fonts.googleapis.com/css2?family=Montserrat:wght@400;500;700&display=swap">
<style>
  :root {
    --page: #e6e2dc;
    --card: #eef1f2;
    --card-edge: #d6dadc;
    --ink: #2a2b2d;
    --teal: #1f7f9e;
    --teal-dark: #14607a;
    --sky: #2ea3d3;
    --rule: #2a8fb5;
  }
  * { margin: 0; padding: 0; box-sizing: border-box; }
  html, body { width: 1200px; height: 897px; overflow: hidden; background: var(--page); }
  body { position: relative; font-family: "Montserrat", sans-serif; color: var(--ink); }

  .card {
    position: absolute; left: 100px; top: 178px;
    width: 1000px; height: 541px;
    background: linear-gradient(160deg, #f4f6f7 0%, var(--card) 60%, #e7ebec 100%);
    border: 1px solid var(--card-edge);
    border-radius: 22px;
    overflow: hidden;
    box-shadow: 0 14px 40px rgba(60, 50, 40, 0.18);
  }

  .wave { position: absolute; left: 0; bottom: 0; width: 1000px; height: 140px; }

  .brand { position: absolute; left: 80px; top: 250px; display: flex; align-items: center; gap: 18px; }
  .brand-mark { width: 58px; height: 58px; background: var(--teal); border-radius: 4px; }
  .brand-name {
    font-weight: 700; font-size: 30px; line-height: 1.1; color: var(--ink);
    letter-spacing: 0.5px;
  }
  .tagline {
    position: absolute; left: 156px; top: 330px;
    font-weight: 400; font-size: 18px; letter-spacing: 0.8px; color: var(--sky);
    text-transform: uppercase;
  }

  .divider { position: absolute; left: 506px; top: 173px; width: 2px; height: 196px; background: var(--rule); }

  .contact { position: absolute; left: 545px; top: 170px; }
  .person-name { font-weight: 700; font-size: 36px; color: var(--teal); letter-spacing: 0.5px; line-height: 1; }
  .license { margin-top: 10px; font-size: 22px; font-weight: 400; }
  .details { list-style: none; margin-top: 26px; }
  .details li { display: flex; align-items: center; gap: 10px; font-size: 22px; height: 38px; }
  .details svg { width: 16px; height: 16px; flex: none; fill: var(--teal); }
</style>
</head>
<body>
  <main class="card" aria-label="Marlow Crest Homes business card">
    <div class="brand">
      <div class="brand-mark" aria-hidden="true"></div>
      <div class="brand-name">MARLOW CREST<br>HOMES</div>
    </div>
    <p class="tagline">Forever Framed Right</p>

    <div class="divider" aria-hidden="true"></div>

    <section class="contact">
      <h1 class="person-name">DEAN MARLOW</h1>
      <p class="license">License: MARLOCH462QT</p>
      <ul class="details">
        <li>
          <svg viewBox="0 0 16 16" aria-hidden="true"><path d="M3.6 1.5l2.3 2.6-1.4 1.8c.9 2 2.5 3.6 4.6 4.6l1.8-1.4 2.6 2.3-1.3 2.1C7.4 13.3 2.7 8.6 1.5 3.8z"/></svg>
          (253) 555-0187
        </li>
        <li>
          <svg viewBox="0 0 16 16" aria-hidden="true"><path d="M1 3h14v1.2L8 8.8 1 4.2z M1 5.8l7 4.6 7-4.6V13H1z"/></svg>
          marlowcresthomes@mailvista.test
        </li>
        <li>
          <svg viewBox="0 0 16 16" aria-hidden="true"><path d="M8 1a7 7 0 100 14A7 7 0 008 1zm0 1.4c.8 0 1.7 1.4 2 3.6H6c.3-2.2 1.2-3.6 2-3.6zM2.5 7h2.6c0 .7 0 1.4.1 2H2.5a5.6 5.6 0 010-2zm3.6 0h3.8a11 11 0 010 2H6.1a11 11 0 010-2zm4.8 0h2.6a5.6 5.6 0 010 2h-2.6c.1-.6.1-1.3 0-2zM6 10h4c-.3 2.2-1.2 3.6-2 3.6S6.3 12.2 6 10z"/></svg>
          www.marlowcresthomes.test
        </li>
      </ul>
    </section>

    <svg class="wave" viewBox="0 0 1000 140" preserveAspectRatio="none" aria-hidden="true">
      <defs>
        <linearGradient id="waveFill" x1="0" y1="0" x2="1" y2="0">
          <stop offset="0" stop-color="#1f7f9e"/>
          <stop offset="0.6" stop-color="#1c88a8"/>
          <stop offset="1" stop-color="#14607a"/>
        </linearGradient>
      </defs>
      <path d="M0 36 C260 70 480 118 700 112 C840 108 940 86 1000 74 L1000 140 L0 140 Z" fill="url(#waveFill)"/>
      <path d="M280 88 C480 120 700 122 820 110 C900 102 960 86 1000 72" fill="none" stroke="#222" stroke-width="4"/>
    </svg>
  </main>
</body>
</html>
```